■依頼の目的/概要
・スーパーの店頭でチーズケーキを販売促進させるためのポスターを作成希望です。前回もクラフタス上で募集しており、今回第2弾の募集となります。
・前回は「月間●本売れた伝説のチーズケーキ」というコピーで作って頂いております(参考までに既存販促ポスター添付しておきます)。今回小売店様から別の販促ポスターを求められており、再度お願いするものです。

■依頼詳細
・ポスター内に貼付のチーズケーキ画像を入れてください。
(写真を使う場合も4つ全て使っていただく必要はありません)
・商品名の「濃厚シルクレアチーズケーキ」「濃厚ほろ蜜チーズケーキ」を入れてください。
・今回は下のセールスコピーのうち、1つもしくは複数を使用し、セールスコピーにあったテイストのデザインにして頂きたいです。なお、下記セールスコピーは全てクラフタス内でお願いし、考えて頂いたものです。
・良いデザインのものがあれば複数当選させたいと思っています。

①専門店にはもう行けない。
⇒スイーツ専門店並みのクオリティの商品ながら価格は半額近く。 コスパが良すぎて、これを買ってしまったら専門店には行けないという趣旨のコピーです。

②このチーズ感、もはや牧場
⇒チーズ生地にクリームチーズを69%配合している濃厚なチーズケーキであるということをコミカルに表現したコピーです。牛の写真やイラストを入れたり、コミカルでパンチのあるポスターにしてもらえたらと思っています。

③濃いから、恋した。
⇒濃厚なチーズケーキに恋をした、という「濃い」と「恋い」をかけたコピーです。お洒落で女性ウケしそうな、しっとりとしたデザインにしたいです。

④売り切れちゃうから、つぶやかないで。
⇒クオリティが高くてコスパが良い商品なので、SNS等で発信しないで!という趣旨のコピーです。

⑤買って後悔。2個買っておけばよかったと。
⇒あえてネガティブなワードを先頭に持ってくることで目を引くようにしたコピーです。

⑥濃くて美味しい、手頃で嬉しい。
⇒商品の良さを語呂よくシンプルに表したコピーです。

その他何かご不明な点がございましたら、お気軽にご質問下さい。
よろしくお願いいたします。
ご提案ありがとうございます。

ごちゃごちゃしたスーパーの売場の中で目を引かせるためには
コピーのインパクトが重要なのかなと思っております。

添付資料としている「伝説のチーズケーキ」のように、
ある程度セールスコピーを大きく目立たせるポスターのほうが好ましいです。

「このチーズ感、もはや牧場」
牛のインパクト、セールスコピーの力強さが売り場で目を引くつくりになっており、
気に入りました。

「もうひとつ買っておけばよかった」
漫画調のデザインが販促ポスターとしては斬新で気に入りました。

「濃いから、恋した」
全体のバランスのよさ、色使いが気にいりました。

数多くのご提案を頂きありがとうございました。

引き続き新商品の販促資料や商品パッケージ等を
クラフタ上で募集してまいりますので、引き続きよろしくお願いいたします。

```html
<!DOCTYPE html>
<html lang="ja">
<head>
<meta charset="UTF-8">
<title>濃いから、恋した。濃厚チーズケーキ</title>
<link rel="stylesheet" href="https://fonts.googleapis.com/css2?family=Shippori+Mincho+B1:wght@600;800&family=Yellowtail&family=Noto+Sans+JP:wght@700&display=swap">
<style>
  :root {
    --bg: #f3f1ef;
    --photo-light: #f6f4f2;
    --photo-mid: #d9d2cc;
    --heart-top: #e3222e;
    --heart-bottom: #b8101c;
    --white: #ffffff;
    --label-black: #141212;
    --gold: #c9a45a;
    --gold-light: #e8cf8f;
    --label-text-dark: #231a10;
  }
  * { margin: 0; padding: 0; box-sizing: border-box; }
  html, body { width: 849px; height: 1200px; overflow: hidden; background: var(--bg); }
  .poster { position: relative; width: 849px; height: 1200px; overflow: hidden; }

  .model-photo { position: absolute; inset: 0; width: 849px; height: 1200px;
    background: linear-gradient(180deg, var(--photo-mid) 0%, var(--photo-light) 45%, var(--bg) 100%); }

  .heart { position: absolute; left: 0; top: 0; width: 849px; height: 1200px; }

  .catch { position: absolute; left: 0; width: 849px; text-align: center; color: var(--white);
    font-family: "Shippori Mincho B1", serif; }
  .catch-lead { top: 385px; font-size: 54px; font-weight: 800; letter-spacing: 2px;
    transform: rotate(-4deg); text-shadow: 0 2px 6px rgba(0,0,0,.25); }
  .catch-title { top: 460px; font-size: 92px; font-weight: 800; letter-spacing: 0;
    transform: rotate(-4deg); text-shadow: 0 3px 8px rgba(0,0,0,.3); }
  .catch-en { top: 590px; font-family: "Yellowtail", cursive; font-size: 58px;
    transform: rotate(-4deg); }

  .product-photo { position: absolute; top: 680px; width: 212px; height: 285px;
    border-radius: 4px; box-shadow: 0 4px 10px rgba(0,0,0,.3); }
  .product-silky { left: 198px; background: linear-gradient(180deg, #e9dfb8 0%, #f0c94a 40%, #e4ae3a 100%); }
  .product-honey { left: 497px; background: linear-gradient(180deg, #e7e2d6 0%, #c8853f 40%, #a4612a 100%); }

  .mini-heart { position: absolute; left: 372px; top: 735px; width: 106px; height: 90px; }
  .mini-heart-text { position: absolute; left: 372px; top: 760px; width: 106px; text-align: center;
    font-family: "Yellowtail", cursive; color: var(--white); font-size: 22px; transform: rotate(-6deg); }

  .label { position: absolute; top: 975px; width: 296px; height: 210px; background: var(--label-black);
    border: 3px solid var(--gold); outline: 1px solid var(--gold); outline-offset: -9px;
    text-align: center; font-family: "Shippori Mincho B1", serif; }
  .label-left { left: 100px; }
  .label-right { left: 468px; }
  .label-main { display: block; margin-top: 18px; color: var(--white); font-size: 60px; font-weight: 800; line-height: 1; letter-spacing: 4px; }
  .label-sub { display: block; margin-top: 10px; color: var(--white); font-size: 30px; font-weight: 600; line-height: 1.1; }
  .label-bar { position: absolute; left: 14px; right: 14px; bottom: 16px; height: 52px;
    background: linear-gradient(180deg, var(--gold-light), var(--gold)); color: var(--label-text-dark);
    font-size: 32px; font-weight: 800; line-height: 52px; letter-spacing: 2px; }
</style>
</head>
<body>
<main class="poster">
  <div class="model-photo" role="img" aria-label="白いジャケットの女性がハートのボードを両手で持つ写真"></div>

  <svg class="heart" viewBox="0 0 849 1200" aria-hidden="true">
    <defs>
      <linearGradient id="heartFill" x1="0" y1="0" x2="0" y2="1">
        <stop offset="0" stop-color="var(--heart-top)"/>
        <stop offset="1" stop-color="var(--heart-bottom)"/>
      </linearGradient>
    </defs>
    <path d="M424 395 C380 300 250 268 150 298 C40 333 8 460 38 565 C88 735 300 905 424 1160 C548 905 760 735 810 565 C840 460 808 333 698 298 C598 268 468 300 424 395 Z" fill="url(#heartFill)"/>
  </svg>

  <p class="catch catch-lead">濃いから、恋した。</p>
  <h1 class="catch catch-title">濃厚チーズケーキ</h1>
  <p class="catch catch-en">Rich Cheese Cake</p>

  <div class="product-photo product-silky" role="img" aria-label="濃厚シルクレアチーズケーキの商品写真"></div>
  <div class="product-photo product-honey" role="img" aria-label="濃厚ほろ蜜チーズケーキの商品写真"></div>

  <svg class="mini-heart" viewBox="0 0 106 90" aria-hidden="true">
    <path d="M53 20 C45 4 22 0 10 12 C-2 25 4 46 20 60 C33 72 46 80 53 88 C60 80 73 72 86 60 C102 46 108 25 96 12 C84 0 61 4 53 20 Z" fill="var(--heart-top)" stroke="var(--white)" stroke-width="3"/>
  </svg>
  <p class="mini-heart-text">Cheese Cake</p>

  <div class="label label-left">
    <span class="label-main">濃厚</span>
    <span class="label-sub">シルクレア</span>
    <span class="label-bar">チーズケーキ</span>
  </div>
  <div class="label label-right">
    <span class="label-main">濃厚</span>
    <span class="label-sub">ほろ蜜</span>
    <span class="label-bar">チーズケーキ</span>
  </div>
</main>
</body>
</html>
```